Bright Harbor Family Club Business Card Project

We are a Minneapolis based discount club that caters to families with children. We need a business card that can be used to communicate our contact information to other businesses that may wish to offer discounts on our website.

Please use placeholders for contact information (i.e. John Doe, 123 Any Street, Any Town, etc.) and include spaces for the following: Full name, title, email, phone number, website, one line street address, city, state, and zip code.

Reason: I have extended the deadline because I had not intended the project to close so quickly.

Target Market(s)

Most of the time the business cards will be used in business to business situations. However, from time to time they may be distributed to our end customer, families with children.

Industry/Entity Type

Club

Font styles to use
Serif
Sans Serif
Other font styles liked:
• Open to suggestions

Requirements
Nice to have
• We might use the reverse side of the card as the design for our membership card.

```html
<!DOCTYPE html>
<html lang="en">
<head>
<meta charset="utf-8">
<title>Bright Harbor Family Club – Business Card</title>
<link rel="stylesheet" href="https://fonts.googleapis.com/css2?family=Arimo:wght@400;700&display=swap">
<style>
  :root {
    --page: #f3f3f3;
    --card-dark: #2f2226;
    --card-mid: #3d3a33;
    --card-green: #4a5c4a;
    --name-red: #c9262c;
    --text-light: #e6e2dc;
    --accent-orange: #ec8a1c;
    --brand-yellow: #f6b318;
    --icon-ink: #2f2226;
  }
  * { margin: 0; padding: 0; box-sizing: border-box; }
  html, body {
    width: 1200px; height: 873px; overflow: hidden;
    background: var(--page);
    font-family: "Arimo", Arial, sans-serif;
  }
  .sheet {
    width: 1200px; height: 873px;
    display: flex; align-items: center; justify-content: center; gap: 50px;
  }
  .card {
    position: relative;
    width: 525px; height: 300px;
    border-radius: 3px; overflow: hidden;
    box-shadow: 0 10px 28px rgba(0,0,0,.22);
  }
  .card-texture {
    position: absolute; inset: 0;
    background:
      radial-gradient(ellipse at 35% 40%, rgba(74,92,74,.75), transparent 60%),
      radial-gradient(ellipse at 75% 70%, rgba(74,92,74,.55), transparent 55%),
      linear-gradient(135deg, var(--card-dark), var(--card-mid) 55%, var(--card-dark));
  }
  .contact {
    position: absolute; left: 34px; top: 26px;
    color: var(--text-light);
  }
  .contact-name {
    color: var(--name-red);
    font-size: 22px; font-weight: 400;
    letter-spacing: .2px;
  }
  .contact-title { font-size: 13px; margin-top: 3px; }
  .contact-list { list-style: none; margin-top: 12px; }
  .contact-list li {
    display: flex; align-items: center; gap: 9px;
    font-size: 12px; line-height: 20px;
  }
  .contact-icon { width: 13px; height: 13px; flex: none; }
  .contact-web {
    color: var(--accent-orange);
    font-size: 12.5px; margin-top: 5px;
  }
  .brand {
    position: absolute;
    display: flex; align-items: center; gap: 10px;
    color: var(--brand-yellow);
    font-weight: 700;
  }
  .brand-dot {
    width: 16px; height: 16px; border-radius: 50%;
    background: var(--brand-yellow); flex: none;
  }
  .card-front .brand { right: 30px; bottom: 24px; font-size: 20px; }
  .card-back .brand {
    left: 50%; top: 50%; transform: translate(-50%, -50%);
    font-size: 28px; white-space: nowrap;
  }
  .card-back .brand-dot { width: 22px; height: 22px; }
</style>
</head>
<body>
<main class="sheet">

  <section class="card card-front">
    <div class="card-texture" role="img" aria-label="Dark scratched grunge texture in brown and muted green"></div>

    <div class="contact">
      <h1 class="contact-name">Daniel Moreno</h1>
      <p class="contact-title">Financial Advisor</p>
      <ul class="contact-list">
        <li>
          <svg class="contact-icon" viewBox="0 0 14 14"><circle cx="7" cy="7" r="7" fill="var(--accent-orange)"/><path d="M7 3.2a2.4 2.4 0 0 0-2.4 2.4c0 1.9 2.4 5 2.4 5s2.4-3.1 2.4-5A2.4 2.4 0 0 0 7 3.2z" fill="var(--icon-ink)"/></svg>
          482 Elm Row street
        </li>
        <li>
          <svg class="contact-icon" viewBox="0 0 14 14"><circle cx="7" cy="7" r="7" fill="var(--accent-orange)"/><path d="M3.5 10.5V6h2.5V3.5h4.5v7z" fill="var(--icon-ink)"/></svg>
          lakeview
        </li>
        <li>
          <svg class="contact-icon" viewBox="0 0 14 14"><circle cx="7" cy="7" r="7" fill="var(--accent-orange)"/><path d="M3.5 7.2 7 4l3.5 3.2V10.5h-7z" fill="var(--icon-ink)"/></svg>
          minnesota
        </li>
        <li>
          <svg class="contact-icon" viewBox="0 0 14 14"><circle cx="7" cy="7" r="7" fill="var(--accent-orange)"/><rect x="4" y="4.5" width="6" height="5" fill="var(--icon-ink)"/></svg>
          55401
        </li>
        <li>
          <svg class="contact-icon" viewBox="0 0 14 14"><circle cx="7" cy="7" r="7" fill="var(--accent-orange)"/><rect x="3.5" y="4.5" width="7" height="5" fill="var(--icon-ink)"/><path d="M3.5 4.5 7 7.3l3.5-2.8" stroke="var(--accent-orange)" stroke-width=".9" fill="none"/></svg>
          dmoreno@mail.com
        </li>
        <li>
          <svg class="contact-icon" viewBox="0 0 14 14"><circle cx="7" cy="7" r="7" fill="var(--accent-orange)"/><path d="M4.6 3.6c.5-.4 1-.3 1.3.2l.6 1.1c.2.4 0 .8-.3 1l-.4.3c.4.9 1 1.5 1.9 1.9l.3-.4c.2-.3.6-.5 1-.3l1.1.6c.5.3.6.8.2 1.3-.6.8-1.5 1-2.4.6A7 7 0 0 1 4 6c-.4-.9-.2-1.8.6-2.4z" fill="var(--icon-ink)"/></svg>
          02 0184 066 312 7
        </li>
      </ul>
      <p class="contact-web">www.brightharborfamilyclub.com</p>
    </div>

    <div class="brand"><span class="brand-dot"></span>Bright Harbor Family Club</div>
  </section>

  <section class="card card-back">
    <div class="card-texture" role="img" aria-label="Dark scratched grunge texture in brown and muted green"></div>
    <div class="brand"><span class="brand-dot"></span>Bright Harbor Family Club</div>
  </section>

</main>
</body>
</html>
```